Business Cards and Stationary for Studio Calmaris (Massage Therapy)
BC for Massage Therapy Studio
Professional
Corwin Palde
President/CEO
742 Fenwick Rd.
Ste. 7C
Greer, SC 48213
cpalde@studiocalmaris.example
www.studiocalmaris.example
Logo AI file

```html
<!DOCTYPE html>
<html lang="en">
<head>
<meta charset="utf-8">
<title>Studio Calmaris – Business Card</title>
<link rel="stylesheet" href="https://fonts.googleapis.com/css2?family=Cinzel:wght@600&family=PT+Sans:wght@400;700&family=PT+Serif:wght@700&display=swap">
<style>
  :root {
    --backdrop: #d9d4cc;
    --card-black: #0c0c0c;
    --card-black-soft: #1b1b1b;
    --gold: #e6c72a;
    --gold-deep: #b8961a;
    --gold-light: #f5e27a;
    --silver: #e4e4e4;
    --silver-dark: #8c8c8c;
    --text-light: #e8e8e8;
    --text-muted: #c9c9c9;
  }
  * { margin: 0; padding: 0; box-sizing: border-box; }
  html, body {
    width: 1200px;
    height: 780px;
    overflow: hidden;
    background: var(--backdrop);
  }
  .card {
    position: absolute;
    left: 60px;
    top: 80px;
    width: 1080px;
    height: 620px;
    border-radius: 36px;
    overflow: hidden;
    background: linear-gradient(135deg, var(--card-black-soft) 0%, var(--card-black) 55%, #050505 100%);
    box-shadow: 0 10px 30px rgba(0,0,0,0.35);
  }
  .edge-band {
    position: absolute;
    left: 0;
    top: 0;
    width: 1080px;
    height: 620px;
  }
  .brand-mark {
    position: absolute;
    left: 530px;
    top: 90px;
    width: 120px;
    height: 120px;
    border-radius: 50%;
    background: var(--gold);
  }
  .brand-name {
    position: absolute;
    left: 300px;
    width: 580px;
    top: 232px;
    text-align: center;
    font-family: "Cinzel", serif;
    font-weight: 600;
    font-size: 46px;
    letter-spacing: 1px;
    color: var(--gold);
  }
  .brand-rule {
    position: absolute;
    left: 360px;
    top: 300px;
    width: 460px;
    height: 2px;
    background: linear-gradient(90deg, var(--gold-deep), var(--gold) 40%, var(--gold-light));
  }
  .person {
    position: absolute;
    left: 352px;
    top: 322px;
    display: flex;
    align-items: baseline;
    gap: 14px;
  }
  .person-name {
    font-family: "PT Serif", serif;
    font-weight: 700;
    font-size: 34px;
    color: var(--gold);
  }
  .person-divider {
    width: 3px;
    height: 34px;
    background: var(--text-light);
    align-self: center;
  }
  .person-title {
    font-family: "PT Sans", sans-serif;
    font-size: 22px;
    color: var(--text-muted);
  }
  .address {
    position: absolute;
    right: 540px;
    top: 404px;
    text-align: right;
    font-family: "PT Sans", sans-serif;
    font-style: normal;
    font-size: 22px;
    line-height: 33px;
    color: var(--text-light);
  }
  .contact-divider {
    position: absolute;
    left: 558px;
    top: 400px;
    width: 2px;
    height: 110px;
    background: var(--text-muted);
  }
  .contact {
    position: absolute;
    left: 576px;
    top: 404px;
    list-style: none;
    font-family: "PT Sans", sans-serif;
    font-size: 22px;
    line-height: 33px;
    color: var(--text-light);
  }
  .contact li {
    display: flex;
    align-items: center;
    gap: 10px;
  }
  .contact-icon {
    width: 20px;
    height: 20px;
    flex: none;
  }
</style>
</head>
<body>
  <div class="card">
    <svg class="edge-band" viewBox="0 0 1080 620" aria-hidden="true">
      <defs>
        <linearGradient id="silverSweep" x1="0" y1="0" x2="1" y2="1">
          <stop offset="0" stop-color="#8c8c8c"/>
          <stop offset="0.5" stop-color="#e4e4e4"/>
          <stop offset="1" stop-color="#ffffff"/>
        </linearGradient>
        <linearGradient id="goldBand" x1="0" y1="0" x2="1" y2="1">
          <stop offset="0" stop-color="#b8961a"/>
          <stop offset="0.45" stop-color="#e6c72a"/>
          <stop offset="0.8" stop-color="#f5e27a"/>
          <stop offset="1" stop-color="#b8961a"/>
        </linearGradient>
      </defs>
      <path d="M0,20 C70,240 110,470 270,620 L222,620 C90,480 40,270 0,70 Z" fill="url(#silverSweep)"/>
      <path d="M0,70 C40,270 80,470 210,620 L0,620 Z" fill="url(#goldBand)"/>
    </svg>

    <div class="brand-mark" aria-hidden="true"></div>
    <div class="brand-name">Studio Calmaris</div>
    <div class="brand-rule"></div>

    <div class="person">
      <span class="person-name">Corwin Palde</span>
      <span class="person-divider"></span>
      <span class="person-title">President/CEO</span>
    </div>

    <address class="address">
      742 Fenwick Rd.<br>
      Ste. 7C<br>
      Larkfield, OR 48213
    </address>

    <div class="contact-divider"></div>

    <ul class="contact">
      <li>
        <svg class="contact-icon" viewBox="0 0 20 20" aria-hidden="true">
          <path d="M5 2 L8 2 L9 6 L7 8 C8 11 9 12 12 13 L14 11 L18 12 L18 15 C18 17 16 18 14 18 C8 17 3 12 2 6 C2 4 3 2 5 2 Z" fill="#e6c72a"/>
        </svg>
        <span>555.204.7318</span>
      </li>
      <li>
        <svg class="contact-icon" viewBox="0 0 20 20" aria-hidden="true">
          <circle cx="10" cy="10" r="9" fill="#e6c72a"/>
          <circle cx="10" cy="10" r="3.5" fill="none" stroke="#0c0c0c" stroke-width="2"/>
          <path d="M13.5 7 L13.5 12 C13.5 14 16 14 16 11 C16 7 13 4 10 4 C6.5 4 4 7 4 10 C4 13.5 7 16 10 16" fill="none" stroke="#0c0c0c" stroke-width="1.8"/>
        </svg>
        <span>cpalde@studiocalmaris.example</span>
      </li>
      <li>
        <svg class="contact-icon" viewBox="0 0 20 20" aria-hidden="true">
          <circle cx="10" cy="10" r="9" fill="#e6c72a"/>
          <ellipse cx="10" cy="10" rx="4" ry="8" fill="none" stroke="#0c0c0c" stroke-width="1.4"/>
          <line x1="2" y1="10" x2="18" y2="10" stroke="#0c0c0c" stroke-width="1.4"/>
        </svg>
        <span>www.studiocalmaris.example</span>
      </li>
    </ul>
  </div>
</body>
</html>
```